Brightmarket Web Demo Clickthru

Create a realistic web demo to demonstrate our Tradeloop Platform.
There is no back end required.
This Demo will shown to Senior M&A or R&D Executives.
Student entrepreneurs will also see this demo.
There are several attachment to this spec.
Two most important are
Demo User Spec and Demo Flow word documents.
Other attaches are images to give you some idea of the content for specific areas of the site. This will require a walkthrough with selected designer.
Updates

Target Market(s)

See Brief

Industry/Entity Type

Venture Capital

Number of Pages Required

5+ page

Font styles to use
Sans Serif

Colors
32a5d7
33a6d7
0255a3
0692cd
85abd2
f37122
000000
474747
919191

Requirements
Must have
• See Brief
Nice to have
• See Briefs
Should not have
• See Briefs

```html
<!DOCTYPE html>
<html lang="en">
<head>
<meta charset="utf-8">
<title>Brightmarket – Tradeloop Platform</title>
<link href="https://fonts.googleapis.com/css2?family=Cinzel:wght@400;700&family=Open+Sans:wght@400;600;700&display=swap" rel="stylesheet">
<style>
:root{
  --sky:#32a5d7;
  --navy:#0255a3;
  --ocean:#0692cd;
  --mist:#85abd2;
  --orange:#f37122;
  --black:#000000;
  --ink:#474747;
  --grey:#919191;
  --paper:#ffffff;
  --pale:#f1f1f1;
  --night:#1d1d1f;
}
*{box-sizing:border-box;margin:0;padding:0}
html,body{width:678px;height:1200px;overflow:hidden}
body{font-family:"Open Sans",Arial,sans-serif;color:var(--ink);background:var(--paper);position:relative}
.serif{font-family:"Cinzel",Georgia,serif}

/* header */
.topbar{height:46px;display:flex;align-items:center;justify-content:space-between;padding:0 14px;background:var(--paper)}
.brand{display:flex;align-items:center;gap:6px}
.brand-dot{width:16px;height:16px;border-radius:50%;background:var(--sky)}
.brand-name{font-size:18px;font-weight:700;color:var(--ocean);line-height:1;display:block}
.brand-tag{font-size:6px;color:var(--grey);display:block;margin-top:2px}
.top-right{display:flex;align-items:center;gap:6px;font-size:9px}
.call{color:var(--grey)}
.call b{color:var(--ink);font-size:12px;margin-left:3px}
.btn-sm{background:var(--night);color:#fff;font-size:7px;padding:4px 8px;border-radius:2px;font-weight:600}
.btn-sm.alt{background:var(--ocean)}

.nav{height:28px;background:var(--sky);display:flex;padding-left:14px}
.nav a{color:#fff;font-size:7.5px;font-weight:600;text-transform:uppercase;padding:0 9px;line-height:28px;text-decoration:none;border-right:1px solid rgba(255,255,255,.35)}
.nav a.active{background:var(--navy)}

/* hero */
.hero{position:relative;height:332px;overflow:hidden}
.hero-art{position:absolute;inset:0;background:radial-gradient(circle at 50% 40%,#8f9296 0%,#4a4d52 28%,#25272b 60%,#151618 100%)}
.login{position:absolute;right:36px;top:26px;width:150px;background:rgba(255,255,255,.95);padding:9px 8px 16px;border-radius:2px}
.login input{display:block;width:100%;height:12px;margin-bottom:5px;border:1px solid #ddd;font-size:5.5px;padding:0 4px;color:var(--grey);font-family:inherit}
.login-go{position:absolute;right:-9px;top:12px;width:18px;height:18px;border-radius:50%;background:var(--sky)}
.hero-copy{position:absolute;left:0;right:0;top:196px;text-align:center;color:#fff}
.hero-copy h1{font-size:21px;font-weight:700;letter-spacing:.5px}
.hero-copy p{font-size:9px;margin-top:4px;font-weight:600}
.btn-orange{display:inline-block;background:var(--orange);color:#fff;font-size:7px;padding:5px 14px;border-radius:2px;margin-top:10px;text-transform:uppercase;font-weight:600}

/* audiences */
.audiences{height:170px;background:var(--pale);display:flex;justify-content:center;gap:90px;padding-top:20px}
.audience{width:200px;text-align:center}
.audience-icon{width:34px;height:34px;border-radius:50%;background:var(--orange);margin:0 auto;display:flex;align-items:center;justify-content:center}
.audience h3{font-size:11px;color:var(--ink);margin-top:12px;letter-spacing:.3px}
.audience p{font-size:5.5px;color:var(--grey);margin-top:4px;line-height:1.5}

/* welcome */
.welcome{height:226px;display:flex;gap:24px;padding:22px 30px 0 60px}
.welcome-photo{width:150px;height:150px;border-radius:50%;background:radial-gradient(circle at 45% 40%,#f4efe2,#c9b89a 55%,#7b6a52);border:4px solid #e5e5e5;flex:none}
.welcome-copy h2{font-size:16px;color:var(--ink);letter-spacing:.4px}
.welcome-copy hr{width:30px;border:0;border-top:2px solid var(--sky);margin:6px 0}
.welcome-copy p{font-size:5.8px;line-height:1.55;color:var(--grey)}
.btn-dark{display:inline-block;background:var(--navy);color:#fff;font-size:7px;padding:5px 10px;border-radius:2px;margin-top:12px;font-family:"Cinzel",Georgia,serif}

/* listings */
.tabs{display:flex;gap:4px;padding:0 22px;border-bottom:2px solid #ddd;height:26px;margin-top:6px}
.tab{font-size:10px;padding:0 10px;line-height:24px;background:#e7e7e7;color:var(--ink);border-radius:3px 3px 0 0;align-self:flex-end}
.tab.active{background:var(--paper);border:1px solid #ddd;border-bottom:0}
.carousel{position:relative;height:150px;display:flex;justify-content:center;gap:18px;padding-top:30px}
.arrow{position:absolute;top:50px;font-size:26px;color:var(--ink)}
.arrow.l{left:8px}.arrow.r{right:8px}
.listing{width:130px}
.listing-badge{height:52px;border:1px solid #ccc;border-radius:3px;display:flex;align-items:center;justify-content:center;background:#fff}
.listing-badge span{display:block;width:82px;height:18px;border-radius:3px}
.listing h4{font-size:8px;margin-top:12px;color:var(--ink)}
.view-all{text-align:center;height:38px}
.view-all span{display:inline-block;background:var(--navy);color:#fff;font-size:7px;padding:5px 12px;border-radius:2px;font-weight:600}

/* footer */
.footer{position:absolute;left:0;right:0;top:1022px;height:158px;background:var(--night);color:#bbb;display:flex;gap:22px;padding:22px 20px 0}
.footer-brand{width:70px;flex:none;display:flex;flex-direction:column;align-items:center;gap:6px;padding-top:6px}
.footer-brand i{display:block;width:22px;height:22px;border-radius:50%;background:var(--sky)}
.footer-brand span{font-size:10px;font-weight:700;color:#fff}
.footer h5{font-size:9px;color:#fff;margin-bottom:8px;letter-spacing:.3px}
.footer h5 em{font-style:normal;color:var(--sky)}
.footer li{list-style:none;font-size:6px;line-height:1.7}
.col-links{width:82px}
.col-contact{width:120px}
.contact-row{display:flex;gap:5px;align-items:center;font-size:6px;margin-bottom:6px}
.col-news{width:150px}
.col-news p{font-size:5.8px;line-height:1.5}
.field{height:13px;background:#fff;margin-top:6px;font-size:5.5px;color:var(--grey);padding:3px 4px}
.btn-sub{height:13px;background:var(--orange);color:#fff;font-size:6px;text-align:center;line-height:13px;margin-top:4px;font-weight:600}
.social{display:flex;align-items:center;gap:5px;font-size:6px;margin-bottom:6px;color:#ddd}
.social i{width:12px;height:12px;border-radius:50%;background:var(--sky);display:block}
.copyright{position:absolute;left:0;right:0;bottom:0;height:20px;background:var(--ocean);color:#fff;font-size:5.5px;text-align:center;line-height:20px}
</style>
</head>
<body>

<header class="topbar">
  <div class="brand">
    <span class="brand-dot"></span>
    <div><span class="brand-name">Brightmarket</span><span class="brand-tag">Tradeloop Platform</span></div>
  </div>
  <div class="top-right">
    <span class="call">Call Us<b>123 456 7890</b></span>
    <span class="btn-sm">SIGN IN</span>
    <span class="btn-sm alt">SIGN UP</span>
  </div>
</header>

<nav class="nav">
  <a class="active">Home</a><a>About</a><a>Join Tradeloop</a><a>My Tradeloop</a><a>Student Companies</a><a>Tradeloop Sponsors</a><a>Contact</a>
</nav>

<section class="hero">
  <div class="hero-art" role="img" aria-label="Dark chalkboard backdrop with a glowing light bulb sketch"></div>
  <form class="login">
    <input value="Username or email">
    <input value="Password">
    <span class="login-go"></span>
  </form>
  <div class="hero-copy">
    <h1 class="serif">Change The Way You Innovate</h1>
    <p>We Helps You Get Your Company To Market Rapidly Insure Greater Success</p>
    <span class="btn-orange">Join Us</span>
  </div>
</section>

<section class="audiences">
  <div class="audience">
    <div class="audience-icon"><svg width="16" height="14" viewBox="0 0 16 14"><path d="M8 1 1 4.5 8 8l7-3.5z M4 6.5v3.5c2 1.6 6 1.6 8 0V6.5" fill="none" stroke="#fff" stroke-width="1.4"/></svg></div>
    <h3 class="serif">For Student Entrepreneurs</h3>
    <p>To help student teams bring early ideas to market with a clear path to grow faster.</p>
  </div>
  <div class="audience">
    <div class="audience-icon"><svg width="16" height="14" viewBox="0 0 16 14"><path d="M2 13V5h4v8M6 13V2h8v11M1 13h14" fill="none" stroke="#fff" stroke-width="1.4"/></svg></div>
    <h3 class="serif">For Large Companies</h3>
    <p>To help large companies find new sources of innovation and lower the cost of growth.</p>
  </div>
</section>

<section class="welcome">
  <div class="welcome-photo" role="img" aria-label="Round photo of a light bulb held up to a bright window"></div>
  <div class="welcome-copy">
    <h2 class="serif">Welcome To Brightmarket</h2>
    <hr>
    <p>Brightmarket is a marketplace that helps young companies meet large firms and bring ideas to market faster. Our platform links student founders with senior leaders who want new products, fresh talent and smart partners. Each listing shows the team, the stage of the work and the market it serves, so buyers can compare options in one place. Sponsors gain early access to startups that fit their plans, while founders gain advice, funding and a clear route to their first big customer. Members can browse listings by field, follow teams they like and arrange calls with a single click. We review each company before it joins, so every profile is complete and current. The result is a simple meeting point where research, growth and investment move forward together, saving time for everyone involved.</p>
    <span class="btn-dark">Read More</span>
  </div>
</section>

<div class="tabs">
  <span class="tab active serif">New Startup Listings</span>
  <span class="tab serif">New Sponsors</span>
  <span class="tab serif">Sponsored Companies</span>
</div>

<section class="carousel">
  <span class="arrow l">&#8249;</span>
  <div class="listing"><div class="listing-badge"><span style="background:var(--navy)"></span></div><h4 class="serif">Business Type</h4></div>
  <div class="listing"><div class="listing-badge"><span style="background:var(--grey)"></span></div><h4 class="serif">Business Type</h4></div>
  <div class="listing"><div class="listing-badge"><span style="background:var(--black)"></span></div><h4 class="serif">Business Type</h4></div>
  <div class="listing"><div class="listing-badge"><span style="background:var(--sky)"></span></div><h4 class="serif">Business Type</h4></div>
  <span class="arrow r">&#8250;</span>
</section>

<div class="view-all"><span>VIEW ALL</span></div>

<footer class="footer">
  <div class="footer-brand"><i></i><span>Brightmarket</span></div>
  <div class="col-links">
    <h5 class="serif">Quick <em>Links</em></h5>
    <ul><li>Home</li><li>About</li><li>Join Tradeloop</li><li>My Tradeloop</li><li>Student Companies</li><li>Tradeloop Sponsors</li><li>Contact</li></ul>
  </div>
  <div class="col-contact">
    <h5 class="serif">Contact <em>Details</em></h5>
    <div class="contact-row"><svg width="8" height="10" viewBox="0 0 8 10"><path d="M4 10S0 5.5 0 4a4 4 0 0 1 8 0c0 1.5-4 6-4 6z" fill="#32a5d7"/></svg><span>12 Market Lane, Suite 4<br>Riverton, ST 00000</span></div>
    <div class="contact-row"><svg width="8" height="8" viewBox="0 0 8 8"><path d="M1 0h2l1 2-1 1a5 5 0 0 0 2 2l1-1 2 1v2a1 1 0 0 1-1 1A7 7 0 0 1 0 1a1 1 0 0 1 1-1z" fill="#32a5d7"/></svg><span>123-456-7890</span></div>
    <div class="contact-row"><svg width="9" height="7" viewBox="0 0 9 7"><rect width="9" height="7" fill="#32a5d7"/><path d="M0 0l4.5 4L9 0" fill="none" stroke="#1d1d1f"/></svg><span>hello@brightmarket.example</span></div>
  </div>
  <div class="col-news">
    <h5 class="serif">Newsletter <em>Signup</em></h5>
    <p>Sign up for news on fresh listings, sponsor updates and upcoming demo days.</p>
    <div class="field">Your Name</div>
    <div class="field">Your Email</div>
    <div class="btn-sub">SUBSCRIBE</div>
  </div>
  <div>
    <h5 class="serif">Follow <em>Us</em></h5>
    <div class="social"><i></i>Friendwall</div>
    <div class="social"><i></i>Chirpline</div>
    <div class="social"><i></i>Circlenet</div>
    <div class="social"><i></i>Snapgrid</div>
  </div>
</footer>
<div class="copyright">Copyright 2015 Brightmarket. All Rights Reserved</div>

</body>
</html>
```